Dental lab wants website to get in touch with dentists, dental surgeons, dental students..

We want an overal informative website so people can now who we are, what we do, how to contact us.
We do NOT focus towards patients, but to primarely to dentists,also dental surgeons, dental students, ... (business to business)
We are an innovative company, who work with highly skilled technicians, as well as highly skilled cadcam operators.
CNC milling, 3D printing, CAD design, is all done in house.
Today we lack a tool to communicate that on the internet, hence the website.
for some ideas about our company you can visit www.facebook.com/labowerin
I also uploaded the logo, the blue color, an flyer we made recently.
Use it as inspiration, but don't just follow that style.
good luck,
Dental
4 page
- homepage, contactpage, who are we, .... When we like the concept, we want to have this website extended and build by the designer. But first we want to have a feel how it can look.

```html
<!DOCTYPE html>
<html lang="en">
<head>
<meta charset="utf-8">
<title>Werin Dental – Dental Laboratory</title>
<link href="https://fonts.googleapis.com/css2?family=Open+Sans:wght@400;600;700;800&display=swap" rel="stylesheet">
<style>
  :root{
    --navy:#2d2b78;
    --ink:#333a44;
    --muted:#8a8f98;
    --line:#e3e4e8;
    --soft:#f1f1f3;
    --footer:#2b2b2e;
    --footer-bar:#222224;
    --white:#ffffff;
  }
  *{box-sizing:border-box;margin:0;padding:0}
  html,body{width:1200px;height:2196px;overflow:hidden;background:var(--white)}
  body{font-family:"Open Sans",Arial,sans-serif;color:var(--ink);position:relative}
  a{color:inherit;text-decoration:none}

  /* header */
  .topbar{height:72px;display:flex;align-items:center;justify-content:space-between;padding:0 48px}
  .brand{font-weight:600;font-size:22px;color:var(--ink);letter-spacing:.3px}
  .account{display:flex;gap:8px;align-items:center}
  .search{width:420px;height:30px;border:1px solid var(--line);border-radius:2px;display:flex;align-items:center;padding-left:10px;gap:8px;font-size:12px;color:var(--muted)}
  .btn-small{height:30px;padding:0 16px;border:1px solid var(--line);background:var(--soft);font-size:11px;font-weight:600;display:flex;align-items:center;letter-spacing:.5px}
  .mainnav{height:40px;background:var(--navy);display:flex;align-items:center;padding:0 48px}
  .mainnav a{color:var(--white);font-size:12px;font-weight:600;letter-spacing:.5px;white-space:nowrap;margin-right:56px}

  /* hero */
  .hero{position:relative;height:476px;background:linear-gradient(100deg,#dfe8f2 0%,#c9d6e6 40%,#aabccf 70%,#8fa2b8 100%)}
  .hero-copy{position:absolute;left:48px;top:150px}
  .hero-copy .eyebrow{font-size:36px;font-weight:800;color:var(--navy);line-height:1.1}
  .hero-copy h1{font-size:40px;font-weight:800;color:var(--navy);line-height:1.1}
  .hero-copy p{font-size:17px;color:var(--navy);margin-top:10px;width:360px;line-height:1.45}
  .btn{display:inline-flex;align-items:center;justify-content:center;height:36px;padding:0 22px;background:var(--navy);color:var(--white);font-size:11px;font-weight:700;letter-spacing:.6px}
  .hero-copy .btn{margin-top:22px}

  /* audiences */
  .audiences{display:flex;justify-content:center;gap:60px;padding-top:50px;height:312px}
  .audience{width:260px;text-align:center}
  .audience svg{width:54px;height:54px}
  .audience h3{font-size:22px;font-weight:400;margin-top:18px;color:var(--ink)}
  .audience p{font-size:11px;color:var(--muted);margin-top:10px;line-height:1.6}
  .audience .more{display:inline-block;margin-top:8px;font-size:12px;font-weight:700;color:var(--navy)}
  .rule{margin:0 48px;border:0;border-top:1px solid var(--line)}

  /* welcome */
  .welcome{text-align:center;height:268px;padding-top:40px}
  .welcome h2{font-size:20px;font-weight:700;color:var(--ink);letter-spacing:.5px}
  .welcome h2::after{content:"";display:block;width:70px;height:2px;background:var(--navy);margin:10px auto 0}
  .welcome p{width:860px;margin:22px auto 0;font-size:12px;color:var(--muted);line-height:1.7}
  .welcome .btn{margin-top:26px}

  /* services */
  .services{background:var(--soft);height:428px;padding:38px 48px 0}
  .services-head{display:flex;align-items:center;justify-content:space-between}
  .services-head h2{font-size:20px;font-weight:800;color:var(--navy)}
  .services-head h2 span{font-size:12px;font-weight:400;color:var(--muted);margin-left:10px}
  .cards{display:flex;gap:24px;margin-top:26px}
  .card{width:258px}
  .card .photo{height:164px;border-radius:2px}
  .card h4{font-size:12px;font-weight:700;margin-top:14px}
  .card p{font-size:11px;color:var(--muted);line-height:1.6;margin-top:6px}

  /* testimonials */
  .testimonials{height:272px;padding-top:28px}
  .section-title{font-size:16px;font-weight:800;color:var(--navy);letter-spacing:.5px;display:flex;align-items:center;justify-content:center;gap:18px}
  .section-title::before,.section-title::after{content:"";width:260px;border-top:1px solid var(--line)}
  .quotes{display:flex;gap:60px;justify-content:center;margin-top:40px}
  .quote{display:flex;gap:24px;width:480px}
  .avatar{width:96px;height:96px;border-radius:50%;flex:none;background:radial-gradient(circle at 50% 40%,#e6dcd4,#b9aaa0)}
  .quote p{font-size:11px;color:var(--muted);line-height:1.6;font-style:italic}
  .quote .name{font-size:11px;font-weight:700;color:var(--ink);margin-top:10px}
  .quote .role{font-size:10px;color:var(--muted)}

  /* footer */
  .footer{background:var(--footer);height:256px;padding:32px 48px 0;display:flex;color:#b5b6ba}
  .footer .col{width:276px;padding-right:36px}
  .footer h5{color:var(--white);font-size:13px;font-weight:700;letter-spacing:.4px;margin-bottom:14px}
  .footer p,.footer li{font-size:11px;line-height:1.75}
  .footer ul{list-style:none}
  .footer .read{color:var(--white);font-weight:600;margin-top:8px;display:block;font-size:11px}
  .contact li{display:flex;gap:8px;align-items:center}
  .contact svg{width:12px;height:12px;flex:none}
  .bottombar{background:var(--footer-bar);height:48px;padding:0 48px;display:flex;align-items:center;justify-content:space-between;color:#8d8e92;font-size:11px}
  .social{display:flex;gap:10px}
  .social span{width:14px;height:14px;border-radius:50%;background:#5a5b60}
</style>
</head>
<body>

<header class="topbar">
  <div class="brand">Werin Dental</div>
  <div class="account">
    <div class="search">
      <svg width="12" height="12" viewBox="0 0 12 12"><circle cx="5" cy="5" r="4" fill="none" stroke="#8a8f98" stroke-width="1.5"/><line x1="8" y1="8" x2="11" y2="11" stroke="#8a8f98" stroke-width="1.5"/></svg>
      Search
    </div>
    <a class="btn-small" href="#">LOGIN</a>
    <a class="btn-small" href="#">REGISTER</a>
  </div>
</header>
<nav class="mainnav">
  <a href="#">HOME</a>
  <a href="#">PROFESSIONAL PRODUCTS</a>
  <a href="#">WHO WE ARE</a>
  <a href="#">WHAT WE DO?</a>
  <a href="#">SERVICES</a>
  <a href="#">CONTACT US</a>
</nav>

<section class="hero" role="img" aria-label="Dental technicians in white coats examining a dental prosthesis in the laboratory">
  <div class="hero-copy">
    <div class="eyebrow">WE ARE AN</div>
    <h1>INNOVATIVE COMPANY</h1>
    <p>who work with highly skilled technicians, as well as highly skilled cadcam operators</p>
    <a class="btn" href="#">READ MORE ABOUT</a>
  </div>
</section>

<section class="audiences">
  <div class="audience">
    <svg viewBox="0 0 54 54" fill="none" stroke="#2d2b78" stroke-width="2.5" stroke-linecap="round">
      <path d="M14 8v14a10 10 0 0 0 20 0V8"/><path d="M24 32v6a8 8 0 0 0 16 0v-8"/><circle cx="40" cy="26" r="4"/>
    </svg>
    <h3>Dentists</h3>
    <p>Aenean lobortis risus id ex iaculis facilisis. Vivamus libero orci a mi pretium varius.</p>
    <a class="more" href="#">Learn more ›</a>
  </div>
  <div class="audience">
    <svg viewBox="0 0 54 54" fill="none" stroke="#2d2b78" stroke-width="2.5" stroke-linejoin="round">
      <path d="M16 8c-6 0-9 5-8 12 1 6 4 8 5 14 1 7 2 12 5 12s3-6 5-10c1-2 2-3 4-3s3 1 4 3c2 4 2 10 5 10s4-5 5-12c1-6 4-8 5-14 1-7-2-12-8-12-5 0-7 3-11 3s-6-3-11-3z"/>
    </svg>
    <h3>Dental Surgeons</h3>
    <p>Aenean lobortis risus id ex iaculis facilisis. Vivamus libero orci a mi pretium varius.</p>
    <a class="more" href="#">Learn more ›</a>
  </div>
  <div class="audience">
    <svg viewBox="0 0 54 54" fill="#2d2b78">
      <path d="M27 10 2 22l25 12 25-12z"/><path d="M13 28v10c4 4 10 6 14 6s10-2 14-6V28l-14 7z"/><rect x="46" y="22" width="2.5" height="14"/>
    </svg>
    <h3>Dental Students</h3>
    <p>Aenean lobortis risus id ex iaculis facilisis. Vivamus libero orci a mi pretium varius.</p>
    <a class="more" href="#">Learn more ›</a>
  </div>
</section>

<hr class="rule">

<section class="welcome">
  <h2>WELCOME TO WERIN DENTAL</h2>
  <p>We are an innovative company, who work with highly skilled technicians, as well as highly skilled cadcam operators. We want a formal website so we can get in touch with dentists, dental surgeons, dental students.</p>
  <a class="btn" href="#">VIEW MORE</a>
</section>

<section class="services">
  <div class="services-head">
    <h2>WHAT WE DO<span>Lorem Ipsum is simply dummy text of the printing and typesetting industry</span></h2>
    <a class="btn" href="#">VIEW MORE SERVICES</a>
  </div>
  <div class="cards">
    <div class="card">
      <div class="photo" role="img" aria-label="Dental prosthesis on a purple base" style="background:linear-gradient(135deg,#4a2a5a,#b0607a)"></div>
      <h4>LOREM IPSUM IS SIMPLY</h4>
      <p>We believe service providing function services, give me more details products.</p>
    </div>
    <div class="card">
      <div class="photo" role="img" aria-label="Dental impression model on the workbench" style="background:linear-gradient(135deg,#c8c3bd,#8f8a86)"></div>
      <h4>LOREM IPSUM IS SIMPLY</h4>
      <p>We believe service providing function services, give me more details products.</p>
    </div>
    <div class="card">
      <div class="photo" role="img" aria-label="Dental instruments in a treatment" style="background:linear-gradient(135deg,#7a3a34,#c9a79a)"></div>
      <h4>LOREM IPSUM IS SIMPLY</h4>
      <p>We believe service providing function services, give me more details products.</p>
    </div>
    <div class="card">
      <div class="photo" role="img" aria-label="Dental technician at work in the laboratory" style="background:linear-gradient(135deg,#9db8d6,#e4ecf4)"></div>
      <h4>LOREM IPSUM IS SIMPLY</h4>
      <p>We believe service providing function services, give me more details products.</p>
    </div>
  </div>
</section>

<section class="testimonials">
  <h2 class="section-title">WHAT OUR CLIENT'S SAY</h2>
  <div class="quotes">
    <div class="quote">
      <div class="avatar" role="img" aria-label="Portrait of a client dentist"></div>
      <div>
        <p>"Lorem ipsum dolor sit amet, consectetur adipiscing elit, sed do eiusmod tempor incididunt ut labore et dolore magna aliqua. Ut enim ad minim veniam, quis nostrud."</p>
        <div class="name">DARREN KORAL</div>
        <div class="role">Dentist, Ghent</div>
      </div>
    </div>
    <div class="quote">
      <div class="avatar" role="img" aria-label="Portrait of a client dental surgeon"></div>
      <div>
        <p>"Lorem ipsum dolor sit amet, consectetur adipiscing elit, sed do eiusmod tempor incididunt ut labore et dolore magna aliqua. Ut enim ad minim veniam, quis nostrud."</p>
        <div class="name">DARREN KORAL</div>
        <div class="role">Dentist, Ghent</div>
      </div>
    </div>
  </div>
</section>

<footer class="footer">
  <div class="col">
    <h5>WHO WE ARE?</h5>
    <p>Lorem Ipsum is simply dummy text of the printing and typesetting industry. Lorem Ipsum has been the industry's standard dummy text ever since the 1500s.</p>
    <a class="read" href="#">Read more »</a>
  </div>
  <div class="col">
    <h5>WELCOME</h5>
    <ul><li>Home</li><li>About Us</li><li>Services</li><li>Blog</li><li>Testimonials</li><li>Contact Us</li></ul>
  </div>
  <div class="col">
    <h5>INFORMATION</h5>
    <ul><li>Terms &amp; Conditions</li><li>Privacy Policy</li><li>Newsletter</li><li>Sitemap</li></ul>
  </div>
  <div class="col contact">
    <h5>CONTACT INFO</h5>
    <ul>
      <li><svg viewBox="0 0 12 12"><path d="M6 1a3.5 3.5 0 0 0-3.5 3.5C2.5 7.5 6 11 6 11s3.5-3.5 3.5-6.5A3.5 3.5 0 0 0 6 1z" fill="#b5b6ba"/></svg>14 Molenstraat, 9000 Ghent</li>
      <li><svg viewBox="0 0 12 12"><path d="M3 1 5 3.5 4 5a6 6 0 0 0 3 3l1.5-1L11 9l-1 2C5 11 1 7 1 2z" fill="#b5b6ba"/></svg>+32 9 123 45 67</li>
      <li><svg viewBox="0 0 12 12"><rect x="1" y="2.5" width="10" height="7" fill="none" stroke="#b5b6ba"/><path d="M1 2.5 6 7l5-4.5" fill="none" stroke="#b5b6ba"/></svg>info@werindental.com</li>
    </ul>
  </div>
</footer>
<div class="bottombar">
  <span>© 2015, Werin Dental. All rights reserved.</span>
  <div class="social"><span></span><span></span><span></span><span></span></div>
</div>

</body>
</html>
```